Letterhead for Midwest Law Firm

Our law firm does estate planning and trust administration in Wisconsin and Illinois. We recently obtained a new logo and need to incorporate it into new stationary. The stationary needs to list out the attorneys at the firm, but we will want 3 variations, one with three attorneys, one with six, and one with six plus the names of states where each is licensed to practice (possibly as an asterisk with notation somewhere towards bottom of page. As with most traditional law practices, letterhead should be conservative and convey predictability and reliability. We view our brand as being primarily reliability, with prestige as a secondary element. We are upmarket, but would like to avoid seeming pretentious or "slick". We are a smaller firm with a personal touch.

Target Market(s)

Affluent Midwestern Americans approaching at or approaching retirement age.

Industry/Entity Type

Legal

Font styles to use
Serif
Sans Serif

Requirements
Must have
• Must use our logo. Must comply with Brennick Legal Guild Ethics rules: https://www.halvorjudic.org/courts/offices/docs/pqmtnv20annotated.pdf. Must be conventional. Must list names of attorneys and provide contact information for firm. Note that we are asking for three designs with very minor variations. Also, designer must provide letterhead in a format that is industry-standard for stationary printers.
Nice to have
• We would appreciate an alternate version that will look reasonable when printed on a black-and-white printer. Designer can use judgment as to whether to have use grayscale, black/white, or something in between.
Should not have
• No "motto" or "visit our website" extraneous materials. putting the website address somewhere is fine, but overall there is a lot of required text, and we'd like to not appear cluttered.

```html
<!DOCTYPE html>
<html lang="en">
<head>
<meta charset="utf-8">
<title>Halloway &amp; Brenner LLP — Letterhead</title>
<link rel="stylesheet" href="https://fonts.googleapis.com/css2?family=Libre+Baskerville:wght@400;700&family=Open+Sans:wght@400;600&display=swap">
<style>
  :root {
    --navy: #2b2a3f;
    --blue: #1a9ad6;
    --gold: #f2b02c;
    --body-grey: #6a6a6a;
    --label-grey: #555555;
    --backdrop: #e4e4e4;
    --paper: #fafafa;
  }
  * { margin: 0; padding: 0; box-sizing: border-box; }
  html, body { width: 1101px; height: 1200px; overflow: hidden; background: var(--backdrop); }
  .sheet {
    position: absolute; left: 140px; top: 20px;
    width: 820px; height: 1160px;
    background: var(--paper);
    box-shadow: 0 6px 24px rgba(0,0,0,0.15);
    overflow: hidden;
  }
  .firm-mark {
    position: absolute; top: 70px; left: 0; width: 820px;
    display: flex; justify-content: center; align-items: center; gap: 14px;
  }
  .firm-mark__dot { width: 34px; height: 34px; border-radius: 50%; background: var(--navy); }
  .firm-mark__name {
    font-family: "Libre Baskerville", serif; font-weight: 700;
    font-size: 24px; color: var(--navy); letter-spacing: 0.2px;
  }
  .roster { position: absolute; top: 156px; left: 0; width: 820px; height: 34px; }
  .roster__person { position: absolute; top: 2px; width: 260px; margin-left: -130px; text-align: center; }
  .roster__name {
    font-family: "Libre Baskerville", serif; font-weight: 700;
    font-size: 12.5px; color: var(--navy); line-height: 14px;
  }
  .roster__role {
    font-family: "Libre Baskerville", serif; font-size: 12px;
    color: var(--blue); line-height: 14px;
  }
  .roster__divider { position: absolute; top: 0; width: 1px; height: 33px; background: var(--gold); }
  .letter {
    position: absolute; left: 82px; top: 282px; width: 656px;
    font-family: "Open Sans", sans-serif; font-size: 12px;
    line-height: 21px; color: var(--body-grey);
  }
  .letter__salutation { margin-bottom: 42px; }
  .letter__para { text-align: justify; margin-bottom: 20px; }
  .signoff { position: absolute; left: 82px; top: 782px; font-family: "Open Sans", sans-serif; }
  .signoff__label { font-size: 12px; font-weight: 600; color: var(--label-grey); }
  .signoff__signature {
    margin-top: 14px; width: 198px; height: 40px;
    background: linear-gradient(90deg, rgba(26,122,190,0.22), rgba(26,122,190,0.08));
    border-radius: 4px;
  }
  .signoff__title { margin-top: 12px; font-size: 12px; color: var(--body-grey); }
  .contact {
    position: absolute; left: 62px; top: 1088px;
    font-family: "Libre Baskerville", serif; font-size: 12px;
    color: var(--navy); line-height: 20px;
  }
  .contact__row { display: flex; align-items: center; gap: 7px; }
  .contact__row svg { flex: none; }
  .contact__gap { width: 10px; }
  .base-rule { position: absolute; left: 0; bottom: 0; width: 820px; }
  .base-rule__accent { height: 3px; background: var(--gold); }
  .base-rule__bar { height: 12px; background: var(--navy); }
</style>
</head>
<body>
  <main class="sheet">
    <header class="firm-mark">
      <span class="firm-mark__dot"></span>
      <span class="firm-mark__name">Halloway &amp; Brenner LLP</span>
    </header>

    <section class="roster">
      <div class="roster__person" style="left:146px">
        <div class="roster__name">THOMAS J. HALLOWAY</div>
        <div class="roster__role">Attorney</div>
      </div>
      <span class="roster__divider" style="left:283px"></span>
      <div class="roster__person" style="left:423px">
        <div class="roster__name">GREGORY L. HALLOWAY</div>
        <div class="roster__role">Attorney</div>
      </div>
      <span class="roster__divider" style="left:562px"></span>
      <div class="roster__person" style="left:686px">
        <div class="roster__name">MARIAN E. TOLLIVER</div>
        <div class="roster__role">Paralegal</div>
      </div>
    </section>

    <article class="letter">
      <p class="letter__salutation">Dear Sir,</p>
      <p class="letter__para">Lorem Ipsum is simply dummy text of the printing and typesetting industry. Lorem Ipsum has been the industry's standard dummy text ever since the 1500s, when an unknown printer took a galley of type and scrambled it to make a type specimen book. It has survived not only five centuries, but also the leap into electronic typesetting, remaining essentially unchanged. It was popularised in the 1960s with the release of Tavrin sheets containing Lorem Ipsum passages, and more recently with desktop publishing software like Quillset Layout including versions of Lorem Ipsum.</p>
      <p class="letter__para">Lorem Ipsum is simply dummy text of the printing and typesetting industry. Lorem Ipsum has been the industry's standard dummy text ever since the 1500s, when an unknown printer took a galley of type and scrambled it to make a type specimen book. It has survived not only five centuries, but also the leap into electronic typesetting, remaining essentially unchanged. It was popularised in the 1960s with the release of Tavrin sheets containing Lorem Ipsum passages, and more recently with desktop publishing software like Quillset Layout including versions of Lorem Ipsum.</p>
      <p class="letter__para">Lorem Ipsum is simply dummy text of the printing and typesetting industry. Lorem Ipsum has been the industry's standard dummy text ever since the 1500s, when an unknown printer took a galley of type and scrambled it to make a type specimen book.</p>
    </article>

    <section class="signoff">
      <p class="signoff__label">Your Name</p>
      <div class="signoff__signature" role="img" aria-label="Handwritten signature of Daniel Oskarsen"></div>
      <p class="signoff__title">CEO &nbsp;|&nbsp; Owner</p>
    </section>

    <footer class="contact">
      <div class="contact__row">
        <svg width="14" height="11" viewBox="0 0 14 11" aria-hidden="true"><path d="M1 4 Q7 -1 13 4 L11 5 L10 3.5 Q7 2.5 4 3.5 L3 5 Z M3.5 5 L10.5 5 L12 10 L2 10 Z" fill="#3aa6e0"/></svg>
        <span>555-301-7420</span>
        <span class="contact__gap"></span>
        <svg width="14" height="11" viewBox="0 0 14 11" aria-hidden="true"><path d="M1 4 Q7 -1 13 4 L11 5 L10 3.5 Q7 2.5 4 3.5 L3 5 Z M3.5 5 L10.5 5 L12 10 L2 10 Z" fill="#3aa6e0"/></svg>
        <span>555-301-7488</span>
      </div>
      <div class="contact__row">
        <svg width="14" height="14" viewBox="0 0 14 14" aria-hidden="true"><path d="M7 1 C4.2 1 2.5 3 2.5 5.3 C2.5 8.5 7 13 7 13 C7 13 11.5 8.5 11.5 5.3 C11.5 3 9.8 1 7 1 Z" fill="#3aa6e0"/><circle cx="7" cy="5.3" r="1.8" fill="#fafafa"/></svg>
        <span>218 W. Corrin Street, Suite 300, Easton, WI&nbsp; 53999</span>
      </div>
    </footer>

    <div class="base-rule" aria-hidden="true">
      <div class="base-rule__accent"></div>
      <div class="base-rule__bar"></div>
    </div>
  </main>
</body>
</html>
```